Vantrel Crest Homes needs a business card

We need a business card for a new company in Canada, Ontario. Our company is all about luxury contraction homes for our clients. Our product and services are custom projects design. Under the business logo that will be created, we want a slogan that will be a memorable phrase for consumers to remember us to tell their friends and relatives.

Additional infomation
- Malcolm Dresvany
- President / Ceo
-519.463.7085

Find point what luxury construction products and services can be done

We like to see colors:
- #663300
- and something other colors or color that would attract the client needs and wants

The final design should communicate leads from new or old clients that will grow our empire. Most of all, we try to work among the budget that clients want

NOTE
- we also need an icon for the business (Example: Instagram, Facebook, and Whatsapp icons)
- We want the company name to be remembered easily for clients and our distributors who would get our orders.
- we need an icon on the business cards: Facebook and Instagram.

Thanks,
Vantrel Crest Homes

```html
<!DOCTYPE html>
<html lang="en">
<head>
<meta charset="utf-8">
<title>Vantrel Crest Homes – Business Card</title>
<link rel="stylesheet" href="https://fonts.googleapis.com/css2?family=Poppins:wght@400;500;700&family=Roboto+Condensed:wght@700&display=swap">
<style>
  :root {
    --stage: #2b2b2c;
    --card: #1b1c1d;
    --brown: #663300;
    --edge: #7a4010;
    --white: #f2f2f2;
    --grey: #c9c9c9;
    --rule: #8a8a8a;
  }
  * { margin: 0; padding: 0; box-sizing: border-box; }
  html, body { width: 1200px; height: 874px; overflow: hidden; }
  body { background: var(--stage); position: relative; font-family: "Poppins", sans-serif; }

  .card {
    position: absolute;
    left: 290px;
    width: 620px;
    height: 354px;
    background: var(--card);
    border-bottom: 3px solid var(--edge);
    box-shadow: 0 10px 24px rgba(0,0,0,.45);
  }
  .card--front { top: 56px; }
  .card--back  { top: 462px; }

  .wordmark {
    position: absolute;
    text-align: center;
    color: var(--brown);
  }
  .wordmark__name {
    font-family: "Poppins", sans-serif;
    font-weight: 700;
    line-height: 1;
    white-space: nowrap;
  }
  .wordmark__tagline {
    font-family: "Roboto Condensed", sans-serif;
    font-weight: 700;
    text-transform: uppercase;
    white-space: nowrap;
    margin-top: 6px;
  }
  .card--front .wordmark { left: 0; right: 0; top: 118px; }
  .card--front .wordmark__name { font-size: 44px; }
  .card--front .wordmark__tagline { font-size: 16px; }

  .social {
    position: absolute;
    top: 248px;
    left: 0; right: 0;
    display: flex;
    justify-content: center;
    gap: 4px;
  }

  .card--back .wordmark { right: 40px; top: 120px; }
  .card--back .wordmark__name { font-size: 36px; }
  .card--back .wordmark__tagline { font-size: 13px; }

  .contact {
    position: absolute;
    left: 52px;
    top: 222px;
  }
  .contact__name { color: var(--brown); font-size: 22px; font-weight: 500; line-height: 1.1; }
  .contact__role { color: var(--grey); font-size: 17px; line-height: 1.3; }
  .contact__phone { color: var(--white); font-size: 16px; margin-top: 12px; }
  .contact__rule {
    position: absolute;
    left: 52px; right: 40px;
    top: 278px;
    height: 1px;
    background: var(--rule);
  }
</style>
</head>
<body>
  <section class="card card--front" aria-label="Card front">
    <div class="wordmark">
      <div class="wordmark__name">Vantrel Crest Homes</div>
      <div class="wordmark__tagline">- Home Renovations - Custom Project Design -</div>
    </div>
    <div class="social" aria-label="Social links">
      <svg width="96" height="30" viewBox="0 0 96 30" aria-hidden="true">
        <circle cx="15" cy="15" r="13" fill="none" stroke="#663300" stroke-width="2"/>
        <circle cx="48" cy="15" r="13" fill="none" stroke="#663300" stroke-width="2"/>
        <circle cx="81" cy="15" r="13" fill="none" stroke="#663300" stroke-width="2"/>
      </svg>
    </div>
  </section>

  <section class="card card--back" aria-label="Card back">
    <div class="wordmark">
      <div class="wordmark__name">Vantrel Crest Homes</div>
      <div class="wordmark__tagline">- Home Renovations - Custom Project Design -</div>
    </div>
    <div class="contact">
      <div class="contact__name">Malcolm Dresvany</div>
      <div class="contact__role">President / Ceo</div>
    </div>
    <div class="contact__rule"></div>
    <div class="contact" style="top:290px">
      <div class="contact__phone">519.463.7085</div>
    </div>
  </section>
</body>
</html>
```